New Business Card Design Project

I need a design for business cards, i am an electrical business called "Tandor Electrical and Communications" i need the cards to be double sided with the company logo on the back (attached) the front needs to say my company name, web site, email address, telephone number, and ABN number and electrical license number. I am open to different arrangements of the information but would like the background to be incorporating something electrical or something that looks smart. open to all additional ideas also.

The company colours are orange and grey see logo attached.

Business Name: Tandor Electrical and Communications
Website: tandorelectricalandcomms.example.au
Email: brent@tandorelectricalandcomms.example.au
Telephone(mobile): 0481203967
ABN: 71829034618
Lic No: 830472F

Target Market(s)

Business entities, Project Managers, Accounts, Clients

Industry/Entity Type

Electrician

Contact Information for Business Card

I need a design for business cards, i am an electrical business called "Tandor Electrical and Communications" i need the cards to be double sided with the company logo on the back (attached) the front needs to say my company name

Font styles to use
Serif
Sans Serif

Colors
f37122
5c5c5c

Requirements
Must have
• Must have the Logo on the back open to different ways of it being on the back but had in mind to keep it central but again open to other options
Nice to have
• A real modern cool background that is eye catching yet contemporary
Should not have
• No backgrounds of a light bulb or plug or anything like that

```html
<!DOCTYPE html>
<html lang="en">
<head>
<meta charset="utf-8">
<title>Tandor Electrical and Communications – Business Card</title>
<link rel="stylesheet" href="https://fonts.googleapis.com/css2?family=Open+Sans:wght@400;700&display=swap">
<style>
  :root {
    --orange: #f37122;
    --orange-light: #f39a52;
    --orange-deep: #e8772a;
    --grey: #5c5c5c;
    --grey-dark: #4a4a4a;
    --ink: #3a3a3a;
    --white: #ffffff;
    --backdrop: #d9d9d7;
  }
  * { margin: 0; padding: 0; box-sizing: border-box; }
  html, body {
    width: 1200px;
    height: 800px;
    overflow: hidden;
    background: var(--backdrop);
    font-family: "Open Sans", Arial, sans-serif;
  }
  .stage {
    position: relative;
    width: 1200px;
    height: 800px;
  }
  .card {
    position: absolute;
    top: 245px;
    width: 540px;
    height: 310px;
    overflow: hidden;
    box-shadow: 0 6px 18px rgba(0, 0, 0, 0.25);
  }

  /* Front side */
  .card-front {
    left: 40px;
    background: linear-gradient(160deg, var(--orange-deep) 0%, var(--orange-light) 45%, var(--orange) 100%);
    color: var(--ink);
  }
  .cord-artwork {
    position: absolute;
    left: 30px;
    top: 14px;
    width: 450px;
    height: 120px;
    border-radius: 8px;
    background: linear-gradient(180deg, rgba(255, 255, 255, 0.18), rgba(255, 255, 255, 0.04));
  }
  .contact {
    position: absolute;
    left: 60px;
    top: 158px;
  }
  .contact-name {
    color: var(--white);
    font-weight: 400;
    font-size: 19px;
    line-height: 1.2;
  }
  .contact-company {
    font-weight: 700;
    font-size: 14px;
    line-height: 1.3;
    margin-top: 2px;
  }
  .contact-list {
    list-style: none;
    margin-top: 16px;
    font-size: 14px;
    line-height: 1.3;
  }
  .contact-list li { margin-bottom: 7px; }
  .contact-label { font-weight: 700; }
  .contact-web {
    color: var(--white);
    font-weight: 700;
    font-size: 15px;
    line-height: 1.3;
    margin-top: 8px;
  }
  .registration {
    position: absolute;
    right: 14px;
    top: 118px;
    writing-mode: vertical-rl;
    transform: rotate(180deg);
    font-size: 10px;
    letter-spacing: 0.3px;
    color: var(--ink);
    white-space: nowrap;
  }

  /* Back side */
  .card-back {
    left: 620px;
    background: linear-gradient(150deg, var(--grey-dark) 0%, var(--grey) 60%, #666 100%);
  }
  .brand {
    position: absolute;
    left: 0;
    right: 0;
    top: 88px;
    text-align: center;
  }
  .brand-name {
    color: var(--white);
    font-weight: 700;
    font-size: 56px;
    letter-spacing: 4px;
    text-transform: uppercase;
    line-height: 1;
  }
  .brand-tagline {
    color: var(--orange);
    font-weight: 700;
    font-size: 15px;
    letter-spacing: 1.5px;
    text-transform: uppercase;
    margin-top: 10px;
  }
  .service-badges {
    position: absolute;
    left: 0;
    right: 0;
    top: 222px;
    display: flex;
    justify-content: center;
    gap: 92px;
  }
  .service-badge {
    width: 30px;
    height: 30px;
    border-radius: 50%;
    background: radial-gradient(circle at 40% 35%, var(--orange-light), var(--orange) 70%);
    box-shadow: 0 2px 4px rgba(0, 0, 0, 0.4);
  }
</style>
</head>
<body>
<main class="stage">
  <section class="card card-front" aria-label="Business card front">
    <div class="cord-artwork" role="img" aria-label="Illustration of a grey plug with a wavy cord running across the top of the card"></div>
    <div class="contact">
      <p class="contact-name">Brent M. Lastname</p>
      <p class="contact-company">Tandor Electrical and Communications</p>
      <ul class="contact-list">
        <li><span class="contact-label">Mobile:</span> 0481 203 967</li>
        <li><span class="contact-label">Email:</span> brent@tandorelectricalandcomms.example.au</li>
      </ul>
      <p class="contact-web">www.tandorelectricalandcomms.example.au</p>
    </div>
    <p class="registration">ABN: 71829034618 &nbsp;Lic No: 830472F</p>
  </section>

  <section class="card card-back" aria-label="Business card back">
    <div class="brand">
      <p class="brand-name">Tandor</p>
      <p class="brand-tagline">Electrical &amp; Communications</p>
    </div>
    <div class="service-badges">
      <span class="service-badge" aria-hidden="true"></span>
      <span class="service-badge" aria-hidden="true"></span>
      <span class="service-badge" aria-hidden="true"></span>
    </div>
  </section>
</main>
</body>
</html>
```